Business Card Design Project

We would like you to create business cards. The color scheme should match our website and logo. I have attached an image of a page of our website, as well as our logo. Please Please include the logo on the left with a similar faded horizontal line, and a blueprint type sketch of a house on cribbing on the right, similar to our website. We like the idea of how this looks. I have attached a third image of an actual house on cribbing (crisscrossed wooden beams). Please include cribbing in the blueprint type sketch.

The information to be included on the business cards is

(name)
214 Fernbrook Avenue
Suite 317
West Orange, NJ 07148
732.418.2093
www.keystonebeamworksofnj.example
info@keystonebeamworksofnj.example

This information can be spaced in any way.

I will also be posting a job for letterhead using the same design as the business cards.

If you need anything other information or I have not been clear enough, please do not hesitate to message me.

Thank you!
Updates

This design project is now open to all designers.  Please message me with any questions.  Thank you.

Industry/Entity Type

House

Requirements
Must have
• 1. Our logo
2. Blueprint type sketch of a house on wooden cribbing.
3. Color scheme to match logo and website.
4. Information provided.

```html
<!DOCTYPE html>
<html lang="en">
<head>
<meta charset="utf-8">
<title>Keystone Beamworks of NJ — Business Cards</title>
<link rel="stylesheet" href="https://fonts.googleapis.com/css2?family=Tinos:wght@400;700&display=swap">
<style>
  :root {
    --orange: #f7941d;
    --orange-deep: #ef8a1a;
    --white: #ffffff;
    --ink: #222222;
    --slate: #3a3a3a;
    --backdrop: #e9e7e4;
    --blueprint-light: #eaf4fb;
    --blueprint-mid: #9cc9ea;
    --blueprint-deep: #4a9fd8;
  }
  * { box-sizing: border-box; margin: 0; padding: 0; }
  html, body {
    width: 1200px; height: 835px; overflow: hidden;
    background: var(--backdrop);
    font-family: "Tinos", "Times New Roman", serif;
  }
  .canvas { position: relative; width: 1200px; height: 835px; }
  .card {
    position: absolute; width: 580px; height: 340px;
    box-shadow: 0 6px 18px rgba(0,0,0,0.22);
    overflow: hidden;
  }

  /* Front */
  .card-front { left: 40px; top: 70px; background: var(--white); }
  .front-band {
    position: absolute; left: 0; top: 172px; width: 225px; height: 52px;
    background: var(--orange);
  }
  .front-accent {
    position: absolute; left: 394px; top: 100px; width: 10px; height: 72px;
    background: var(--orange);
  }
  .blueprint {
    position: absolute; left: 410px; top: 100px; width: 170px; height: 72px;
    background: linear-gradient(90deg, var(--blueprint-light) 0%, var(--blueprint-mid) 60%, var(--blueprint-deep) 100%);
  }
  .brand {
    position: absolute; left: 228px; top: 118px; width: 160px;
    text-align: center; color: var(--slate);
  }
  .brand-name {
    display: flex; align-items: center; justify-content: center; gap: 6px;
    font-size: 19px; font-weight: 700; line-height: 1.1; color: var(--slate);
  }
  .brand-mark { width: 10px; height: 10px; background: var(--orange); flex: none; }
  .services {
    margin-top: 8px; font-size: 8.5px; color: var(--orange-deep); letter-spacing: 0.2px;
  }
  .contact-front {
    position: absolute; left: 200px; top: 238px; width: 200px;
    text-align: center; color: var(--ink);
  }
  .contact-front .person { font-size: 15px; line-height: 1.2; }
  .contact-front .phone { font-size: 17px; line-height: 1.3; }

  /* Back */
  .card-back { left: 580px; top: 420px; background: var(--orange); }
  .web-band {
    position: absolute; left: 0; top: 172px; width: 292px; height: 68px;
    background: var(--white);
    display: flex; align-items: center; padding-left: 18px;
  }
  .web-band a {
    font-size: 15.5px; font-weight: 700; color: var(--ink); text-decoration: none;
  }
  .address {
    position: absolute; left: 310px; top: 182px;
    font-size: 16px; line-height: 19px; color: var(--ink); font-style: normal;
  }
  .email { margin-top: 12px; }
</style>
</head>
<body>
<main class="canvas">
  <section class="card card-front" aria-label="Business card front">
    <div class="front-band"></div>
    <div class="front-accent"></div>
    <div class="blueprint" role="img" aria-label="Blueprint-style line sketch of a house raised on wooden cribbing"></div>
    <div class="brand">
      <div class="brand-name"><span class="brand-mark"></span><span>Keystone Beamworks of NJ</span></div>
      <div class="services">House Raising • Construction • Masonry</div>
    </div>
    <div class="contact-front">
      <p class="person">xxxx xxxxx</p>
      <p class="phone">(732) 418-2093</p>
    </div>
  </section>

  <section class="card card-back" aria-label="Business card back">
    <div class="web-band"><a href="#">www.keystonebeamworksofnj.example</a></div>
    <address class="address">
      214 Fernbrook Avenue<br>
      Suite 317<br>
      West Orange<br>
      NJ 07148<br>
      732.418.2093
      <div class="email">info@keystonebeamworksofnj.example</div>
    </address>
  </section>
</main>
</body>
</html>
```